Design for "Quiver" protein health bars wrappers

I need a new design for a protein bar that my partners and I are launching for the North American and European markets.
The bar's name is "Quiver."
Given the masculine/aggressive nature of that name, we are thinking of neutralizing it with a more feminine/soft font and design. But hey - the sky is the limit. We obviously want this 20-gram protein bar to sell to a wide net (not just men but women also). So if it means having a Zephyr Panel font/design (or whatever) in order to do this, so be it. I leave it up to your intelligence and experience.

The official name of the bar is just "QUIVER" (not "Quiver Protein").

We have six flavors divided into two categories, which are 1) SOFT and 2) CRUNCHY.
So, the idea is to make two similar designs for the wrapper that still distinguish themselves from each other because one is 'soft' and the other is 'crunchy.'
Then, within each category, the idea is to have three color variations, designating the three flavors in each category.

Please look at the dimensions and examples of the generic wrapper designs that we already have (and which we find too generic), which I have uploaded.

Target Market(s)

North America - Valmart, Green Basket
Europe - Norway, Sweden, Denmark, Germany, France, Switzerland, Italy.

Industry/Entity Type

Nutrition

Logo Text

Quiver

Font styles to use
Serif
Decorative

Colors
fff6dc
f04a50

Requirements
Must have
• The title is "Quiver".
• We have six flavors divided into two categories, which are 1) SOFT and 2) CRUNCHY.
• You can work on the two different types of similar-but-different designs for the "soft" and for the "cruncy." Then it's just a question of color variations for each flavor.
• The flavors are:
• SOFT: 1) strawberry, 2) Chocolate brownie, 3) Cinnamon Crunch
• CRUNCY: 1) Peanut, 2) Lemon, 3) Coconut.
• On the side or at the bottom, there should be stated:
• "20 gm protein"
• "children friendly"
Nice to have
• Obvious: a design that catches the eye and inspires someone to buy the bar to eat it.
• Part of the design could include a photograph of the actual bar (you can use generic photos for that until we place a pic of the actual bar). Like 1/4th of the total surface (or even a little smaller).

```html
<!DOCTYPE html>
<html lang="en">
<head>
<meta charset="utf-8">
<title>Quiver — Soft Range Wrappers</title>
<link rel="stylesheet" href="https://fonts.googleapis.com/css2?family=Antonio:wght@200;300;400&family=Barlow+Condensed:wght@400&display=swap">
<style>
  :root{
    --canvas:#ffffff;
    --logo-grey:#9d9d9b;
    --cream:#ebe7dc;
    --protein-grey:#8a8884;

    --brownie-band:#4a2f22;
    --brownie-line:#3a2218;
    --brownie-mark:#5b2a10;
    --brownie-photo:#6a3a1c;
    --brownie-photo-dark:#4a2612;
    --brownie-flavour:#c98624;

    --berry-band:#8e2b47;
    --berry-line:#6e1f35;
    --berry-mark:#a52a3c;
    --berry-photo:#b8333f;
    --berry-photo-dark:#8f2433;
    --berry-flavour:#ea5a62;

    --cinnamon-band:#d89c67;
    --cinnamon-line:#c4814a;
    --cinnamon-mark:#c4712c;
    --cinnamon-photo:#b8743c;
    --cinnamon-photo-dark:#8f5426;
    --cinnamon-flavour:#b0652a;

    --soft-white:#ffffff;
  }
  *{margin:0;padding:0;box-sizing:border-box}
  html,body{width:1200px;height:1200px;overflow:hidden;background:var(--canvas)}
  .board{position:relative;width:1200px;height:1200px}
  .brand-header{position:absolute;left:0;top:40px;width:1200px;text-align:center}
  .brand-header__name{
    font-family:'Antonio',sans-serif;font-weight:300;font-size:150px;line-height:128px;
    letter-spacing:14px;color:var(--logo-grey);padding-left:14px;
  }
  .brand-header__claim{
    font-family:'Barlow Condensed',sans-serif;font-weight:400;font-size:18px;
    letter-spacing:1px;color:var(--protein-grey);margin-top:14px;
  }
  .wrapper{position:absolute;left:160px;width:888px;height:240px;display:block}
  .wrapper--brownie{top:252px}
  .wrapper--berry{top:552px}
  .wrapper--cinnamon{top:852px}
  .range-label{font-family:'Antonio',sans-serif;font-weight:300;fill:var(--soft-white)}
  .range-note{font-family:'Barlow Condensed',sans-serif;font-weight:400;font-size:13px;fill:var(--soft-white);letter-spacing:.3px}
  .wordmark{font-family:'Antonio',sans-serif;font-weight:300}
  .protein-claim{font-family:'Barlow Condensed',sans-serif;font-weight:400;font-size:24px;fill:var(--protein-grey);letter-spacing:1.5px}
  .flavour-name{font-family:'Barlow Condensed',sans-serif;font-weight:400}
</style>
</head>
<body>
<svg width="0" height="0" style="position:absolute" aria-hidden="true">
  <defs>
    <clipPath id="crimp-outline">
      <path d="M12 0 l-12 6 12 6 l-12 6 12 6 l-12 6 12 6 l-12 6 12 6 l-12 6 12 6 l-12 6 12 6 l-12 6 12 6 l-12 6 12 6 l-12 6 12 6 l-12 6 12 6 l-12 6 12 6 l-12 6 12 6 l-12 6 12 6 l-12 6 12 6 l-12 6 12 6 l-12 6 12 6 l-12 6 12 6 l-12 6 12 6 l-12 6 12 6 l-12 6 12 6 H876 l12 -6 -12 -6 l12 -6 -12 -6 l12 -6 -12 -6 l12 -6 -12 -6 l12 -6 -12 -6 l12 -6 -12 -6 l12 -6 -12 -6 l12 -6 -12 -6 l12 -6 -12 -6 l12 -6 -12 -6 l12 -6 -12 -6 l12 -6 -12 -6 l12 -6 -12 -6 l12 -6 -12 -6 l12 -6 -12 -6 l12 -6 -12 -6 l12 -6 -12 -6 l12 -6 -12 -6 l12 -6 -12 -6 l12 -6 -12 -6 Z"/>
    </clipPath>
    <pattern id="band-lines" width="6" height="240" patternUnits="userSpaceOnUse">
      <rect x="0" y="0" width="1" height="240" fill="#000" opacity=".18"/>
    </pattern>
  </defs>
</svg>

<main class="board">
  <header class="brand-header">
    <div class="brand-header__name">QUIVER</div>
    <div class="brand-header__claim">20 GM PROTEIN</div>
  </header>

  <!-- Chocolate brownie -->
  <svg class="wrapper wrapper--brownie" viewBox="0 0 888 240" aria-label="Quiver soft chocolate brownie wrapper">
    <g clip-path="url(#crimp-outline)">
      <rect class="band" x="0" y="0" width="190" height="240" fill="var(--brownie-band)"/>
      <rect x="60" y="0" width="100" height="240" fill="url(#band-lines)"/>
      <rect class="label-panel" x="190" y="0" width="382" height="240" fill="var(--cream)"/>
      <rect x="572" y="0" width="316" height="240" fill="var(--brownie-photo)"/>
      <rect x="640" y="0" width="248" height="240" fill="var(--brownie-photo-dark)" role="img" aria-label="Photo of chocolate brownie pieces"/>
    </g>
    <text class="range-label" x="120" y="88" font-size="64" textLength="62" lengthAdjust="spacingAndGlyphs">SOFT</text>
    <text class="range-note" x="120" y="110">CHILDREN</text>
    <text class="range-note" x="120" y="126">FRIENDLY</text>
    <text class="wordmark" x="212" y="216" font-size="240" fill="var(--brownie-mark)" textLength="320" lengthAdjust="spacingAndGlyphs">QUIVER</text>
    <text class="protein-claim" transform="translate(548 36) rotate(90)" textLength="172" lengthAdjust="spacingAndGlyphs">20 MG PROTEIN</text>
    <text class="flavour-name" transform="translate(630 36) rotate(90)" font-size="44" fill="var(--brownie-flavour)">
      <tspan x="0" y="0" textLength="178" lengthAdjust="spacingAndGlyphs">CHOCOLATE</tspan>
      <tspan x="0" y="42" textLength="178" lengthAdjust="spacingAndGlyphs">BROWNIE</tspan>
    </text>
  </svg>

  <!-- Strawberry -->
  <svg class="wrapper wrapper--berry" viewBox="0 0 888 240" aria-label="Quiver soft strawberry wrapper">
    <g clip-path="url(#crimp-outline)">
      <rect x="0" y="0" width="190" height="240" fill="var(--berry-band)"/>
      <rect x="60" y="0" width="100" height="240" fill="url(#band-lines)"/>
      <rect x="190" y="0" width="382" height="240" fill="var(--cream)"/>
      <rect x="572" y="0" width="316" height="240" fill="var(--berry-photo)"/>
      <rect x="660" y="0" width="228" height="240" fill="var(--berry-photo-dark)" role="img" aria-label="Photo of fresh strawberries"/>
    </g>
    <text class="range-label" x="120" y="88" font-size="64" textLength="62" lengthAdjust="spacingAndGlyphs">SOFT</text>
    <text class="range-note" x="120" y="110">CHILDREN</text>
    <text class="range-note" x="120" y="126">FRIENDLY</text>
    <text class="wordmark" x="212" y="216" font-size="240" fill="var(--berry-mark)" textLength="320" lengthAdjust="spacingAndGlyphs">QUIVER</text>
    <text class="protein-claim" transform="translate(548 36) rotate(90)" textLength="172" lengthAdjust="spacingAndGlyphs">20 MG PROTEIN</text>
    <text class="flavour-name" transform="translate(650 30) rotate(90)" font-size="62" fill="var(--berry-flavour)">
      <tspan x="0" y="0" textLength="180" lengthAdjust="spacingAndGlyphs">STRAW</tspan>
      <tspan x="0" y="58" textLength="170" lengthAdjust="spacingAndGlyphs">BERRY</tspan>
    </text>
  </svg>

  <!-- Cinnamon -->
  <svg class="wrapper wrapper--cinnamon" viewBox="0 0 888 240" aria-label="Quiver soft cinnamon wrapper">
    <g clip-path="url(#crimp-outline)">
      <rect x="0" y="0" width="190" height="240" fill="var(--cinnamon-band)"/>
      <rect x="60" y="0" width="100" height="240" fill="url(#band-lines)"/>
      <rect x="190" y="0" width="382" height="240" fill="var(--cream)"/>
      <rect x="572" y="0" width="316" height="240" fill="var(--cinnamon-photo)"/>
      <rect x="630" y="0" width="258" height="240" fill="var(--cinnamon-photo-dark)" opacity=".55" role="img" aria-label="Photo of cinnamon sticks"/>
    </g>
    <text class="range-label" x="120" y="88" font-size="64" textLength="62" lengthAdjust="spacingAndGlyphs">SOFT</text>
    <text class="range-note" x="120" y="110">CHILDREN</text>
    <text class="range-note" x="120" y="126">FRIENDLY</text>
    <text class="wordmark" x="212" y="216" font-size="240" fill="var(--cinnamon-mark)" textLength="320" lengthAdjust="spacingAndGlyphs">QUIVER</text>
    <text class="protein-claim" transform="translate(548 36) rotate(90)" textLength="172" lengthAdjust="spacingAndGlyphs">20 MG PROTEIN</text>
    <text class="flavour-name" transform="translate(588 36) rotate(90)" font-size="44" fill="var(--cinnamon-flavour)" textLength="186" lengthAdjust="spacingAndGlyphs">CINNAMON</text>
  </svg>
</main>
</body>
</html>
```